Roofing Contractor business card redesign

I want to redesign my business card with a fresh, eye catching concept

Target Market(s)

Residential Roofing Clients, potential employees, and subcontractors.

Industry/Entity Type

Business

Colors

Designer to choose colors to be used in the design.

Requirements
Nice to have
• I just want something that's more pleasing to the eye. You can use a combination of either / or of my logos.

```html
<!DOCTYPE html>
<html lang="en">
<head>
<meta charset="utf-8">
<title>Fair Hands Builders – Business Card</title>
<link href="https://fonts.googleapis.com/css2?family=Open+Sans:wght@400;600;700;800&display=swap" rel="stylesheet">
<style>
  :root {
    --stage: #5d5d5d;
    --yellow: #fcc90c;
    --gold: #e5ab08;
    --brown: #3f1e1b;
    --brown-mid: #6b3a1d;
    --orange: #e0783a;
    --white: #ffffff;
    --muted: #c9c9c9;
  }
  * { box-sizing: border-box; margin: 0; padding: 0; }
  html, body {
    width: 1200px; height: 1200px; overflow: hidden;
    background: var(--stage);
    font-family: "Open Sans", Arial, sans-serif;
  }
  .canvas {
    width: 1200px; height: 1200px;
    display: flex; justify-content: center; align-items: center; gap: 80px;
  }
  .card {
    width: 440px; height: 782px; position: relative; overflow: hidden;
    box-shadow: 0 10px 30px rgba(0,0,0,.25);
  }

  /* Back side */
  .card--back {
    background: linear-gradient(180deg, var(--yellow) 0%, var(--gold) 30%, #8a5a14 52%, #53291f 70%, var(--brown) 100%);
    color: var(--white);
  }
  .card--back::before {
    content: ""; position: absolute; inset: 0;
    background: linear-gradient(160deg, rgba(255,230,100,.35) 0%, rgba(255,230,100,0) 40%);
  }
  .brand-lockup { position: absolute; left: 0; right: 0; text-align: center; }
  .card--back .brand-lockup { top: 200px; }
  .brand-name {
    font-weight: 800; color: var(--brown); line-height: 1; letter-spacing: -1px;
    display: inline-flex; align-items: center; gap: 12px;
  }
  .card--back .brand-name { font-size: 46px; }
  .brand-dot { width: 42px; height: 42px; border-radius: 50%; background: var(--brown); display: inline-block; }
  .brand-sub { font-weight: 700; color: var(--brown); }
  .card--back .brand-sub { font-size: 18px; margin-top: 8px; }

  .contact-list {
    position: absolute; left: 28px; top: 475px; list-style: none;
    font-size: 22px; line-height: 31px; position: absolute; z-index: 1;
  }
  .contact-list li { display: flex; align-items: flex-start; gap: 10px; }
  .contact-icon {
    flex: none; width: 22px; height: 22px; margin-top: 5px;
    background: var(--yellow); border-radius: 3px;
    display: flex; align-items: center; justify-content: center;
  }
  .divider {
    position: absolute; left: 75px; right: 84px; top: 674px;
    border-top: 1px solid rgba(255,255,255,.45);
  }
  .get-in-touch {
    position: absolute; top: 712px; left: 0; right: 0;
    display: flex; justify-content: center; align-items: center; gap: 12px;
    font-size: 14px; font-weight: 700; letter-spacing: .5px;
  }
  .social-box { width: 26px; height: 26px; border: 2px solid var(--white); border-radius: 5px; }
  .get-in-touch .label { margin-right: 8px; }

  /* Front side */
  .card--front { background: var(--white); text-align: center; }
  .emblem {
    position: absolute; left: 80px; top: 91px; width: 280px; height: 280px;
    border-radius: 50%; border: 14px solid var(--brown);
    background: radial-gradient(circle at 50% 40%, #f7d34a 0%, #e98a3a 45%, #8a4326 80%);
  }
  .card--front .brand-lockup { top: 392px; }
  .card--front .brand-name { font-size: 58px; }
  .card--front .brand-sub { font-size: 22px; margin-top: 6px; }
  .person-icon { position: absolute; left: 195px; top: 528px; }
  .rep-name {
    position: absolute; top: 618px; left: 0; right: 0;
    font-size: 38px; font-weight: 800; color: var(--brown);
  }
  .rep-titles {
    position: absolute; top: 672px; left: 0; right: 0;
    font-size: 22px; line-height: 28px; color: var(--orange);
  }
</style>
</head>
<body>
<main class="canvas">

  <section class="card card--back">
    <div class="brand-lockup">
      <div class="brand-name">Fair <span class="brand-dot"></span> Hands</div>
      <div class="brand-sub">Builders, Inc.</div>
    </div>

    <ul class="contact-list">
      <li><span class="contact-icon"><svg width="12" height="16" viewBox="0 0 12 16"><rect x="1.5" y="1" width="9" height="14" rx="1.5" fill="none" stroke="#3f1e1b" stroke-width="2"/></svg></span>(555) 210-4471</li>
      <li><span class="contact-icon"><svg width="14" height="14" viewBox="0 0 14 14"><path d="M3 1l3 3-1.5 2a8 8 0 0 0 3.5 3.5L10 8l3 3-2 2C6 13 1 8 1 3z" fill="#3f1e1b"/></svg></span>(555) 210-4000</li>
      <li><span class="contact-icon"><svg width="14" height="11" viewBox="0 0 14 11"><rect x="1" y="1" width="12" height="9" fill="none" stroke="#3f1e1b" stroke-width="1.6"/><path d="M1 1l6 5 6-5" fill="none" stroke="#3f1e1b" stroke-width="1.6"/></svg></span>sam@fairhandstx.com</li>
      <li><span class="contact-icon"><svg width="14" height="13" viewBox="0 0 14 13"><path d="M7 1l6 5.5h-2V12H3V6.5H1z" fill="#3f1e1b"/></svg></span>www.fairhandsbuilders.com</li>
      <li><span class="contact-icon"><svg width="12" height="16" viewBox="0 0 12 16"><path d="M6 1a5 5 0 0 1 5 5c0 4-5 9-5 9S1 10 1 6a5 5 0 0 1 5-5z" fill="#3f1e1b"/><circle cx="6" cy="6" r="2" fill="#fcc90c"/></svg></span><span>4810 Maple Ridge Road Suite, 203<br>Springdale, TX 75010</span></li>
    </ul>

    <div class="divider"></div>
    <div class="get-in-touch">
      <span class="label">GET IN TOUCH</span>
      <span class="social-box"></span>
      <span class="social-box"></span>
    </div>
  </section>

  <section class="card card--front">
    <div class="emblem" role="img" aria-label="Round company emblem illustration of three builders in front of a roof"></div>
    <div class="brand-lockup">
      <div class="brand-name">Fair Hands</div>
      <div class="brand-sub">Builders, Inc.</div>
    </div>
    <svg class="person-icon" width="50" height="56" viewBox="0 0 50 56" aria-hidden="true">
      <circle cx="25" cy="17" r="13" fill="none" stroke="#c9c9c9" stroke-width="2.5"/>
      <path d="M3 53c0-12 10-19 22-19s22 7 22 19z" fill="none" stroke="#c9c9c9" stroke-width="2.5" stroke-linejoin="round"/>
    </svg>
    <div class="rep-name">Sam Whitlock</div>
    <div class="rep-titles">Hartline Certified Roof Inspector<br>Licensed Property Adjuster</div>
  </section>

</main>
</body>
</html>
```